'Gravelmoth Co' Business Cards

Gravelmoth Co is a clothing company geared toward people in the mining industry who are crushing it (literally) We need a design for a business card that has 'GM' similar to the layout of the inspo photo below. Rock textures and maybe some rock dust (see GIF). I Included SVG of our circle logo but not sure how to include without it being boring, would like some ideas. Front should say 'Gravelmoth Co.' (and 'clothing' in smaller letters below) Back should have our webpage 'gravelmothco.ca' our email 'info@gravelmothco.ca' plus a FB and IG icon

```html
<!DOCTYPE html>
<html lang="en">
<head>
<meta charset="utf-8">
<title>Gravelmoth Co — Business Cards</title>
<link rel="stylesheet" href="https://fonts.googleapis.com/css2?family=Archivo:wght@400;700;800&display=swap">
<style>
  :root {
    --backdrop: #e6e6e4;
    --rock-light: #a8a89c;
    --rock-mid: #7d7b6c;
    --rock-dark: #4f4c40;
    --rock-cool: #8e9a9c;
    --emblem-top: #6e675a;
    --emblem-bottom: #2e2920;
    --ink: #ffffff;
    --ink-soft: rgba(255,255,255,0.85);
  }
  * { box-sizing: border-box; margin: 0; padding: 0; }
  html, body { width: 1200px; height: 801px; overflow: hidden; }
  body {
    background: var(--backdrop);
    font-family: "Archivo", Arial, sans-serif;
    color: var(--ink);
    display: flex;
    align-items: center;
    justify-content: center;
    gap: 50px;
  }
  .card {
    position: relative;
    width: 520px;
    height: 297px;
    overflow: hidden;
    box-shadow: 0 10px 24px rgba(0,0,0,0.18);
  }
  .rock-texture {
    position: absolute; inset: 0;
    background:
      radial-gradient(ellipse at 20% 70%, var(--rock-cool) 0%, transparent 45%),
      radial-gradient(ellipse at 80% 20%, var(--rock-light) 0%, transparent 50%),
      linear-gradient(160deg, var(--rock-mid) 0%, var(--rock-light) 45%, var(--rock-mid) 70%, var(--rock-dark) 100%);
  }
  .wordmark {
    position: absolute;
    font-weight: 800;
    letter-spacing: 0.02em;
    text-transform: uppercase;
    color: var(--ink);
    white-space: nowrap;
    line-height: 1;
  }

  /* Contact side */
  .card--contact .wordmark { right: 32px; top: 104px; font-size: 30px; }
  .brand-dot {
    position: absolute;
    left: 124px; top: 72px;
    width: 60px; height: 60px;
    border-radius: 50%;
    background: var(--ink);
  }
  .divider {
    position: absolute;
    height: 1px;
    background: var(--ink-soft);
  }
  .divider--brand { left: 200px; right: 30px; top: 150px; }
  .social {
    position: absolute;
    right: 32px; top: 162px;
    display: flex; gap: 8px;
  }
  .social-dot {
    width: 14px; height: 14px;
    border-radius: 50%;
    border: 1.5px solid var(--ink);
  }
  .person { position: absolute; left: 32px; bottom: 86px; }
  .person-name { font-weight: 700; font-size: 15px; letter-spacing: 0.04em; text-transform: uppercase; }
  .person-role { font-size: 13px; color: var(--ink-soft); margin-top: 2px; }
  .divider--person { left: 32px; width: 260px; bottom: 76px; }
  .contact-list {
    position: absolute; left: 32px; bottom: 22px;
    list-style: none;
    font-size: 14px;
    line-height: 1.55;
  }
  .contact-list li { display: flex; align-items: center; gap: 8px; }
  .contact-list svg { width: 12px; height: 12px; flex: none; }

  /* Brand side */
  .brand-emblem {
    position: absolute;
    left: -20px; top: 60px;
    width: 220px; height: 220px;
    border-radius: 50%;
    background: linear-gradient(170deg, var(--emblem-top) 0%, var(--emblem-bottom) 100%);
    box-shadow: inset 0 2px 3px rgba(255,255,255,0.25), 0 2px 6px rgba(0,0,0,0.35);
  }
  .brand-lockup {
    position: absolute;
    right: 28px; bottom: 48px;
    text-align: right;
  }
  .card--brand .wordmark { position: static; font-size: 30px; }
  .tagline {
    margin-top: 6px;
    font-size: 13px;
    font-weight: 400;
    letter-spacing: 0.3em;
    text-transform: lowercase;
    color: var(--ink-soft);
  }
</style>
</head>
<body>
  <section class="card card--contact">
    <div class="rock-texture" role="img" aria-label="Grey and olive rock surface texture"></div>
    <span class="brand-dot" aria-hidden="true"></span>
    <div class="wordmark">Gravelmoth Co.</div>
    <div class="divider divider--brand"></div>
    <div class="social" aria-label="Social profiles">
      <span class="social-dot"></span>
      <span class="social-dot"></span>
    </div>
    <div class="person">
      <p class="person-name">Dorian Kestrel</p>
      <p class="person-role">Manager</p>
    </div>
    <div class="divider divider--person"></div>
    <ul class="contact-list">
      <li>
        <svg viewBox="0 0 12 12" aria-hidden="true"><rect x="0.5" y="2" width="11" height="8" fill="none" stroke="#fff"/><path d="M0.5 2 L6 6.5 L11.5 2" fill="none" stroke="#fff"/></svg>
        info@gravelmothco.ca
      </li>
      <li>
        <svg viewBox="0 0 12 12" aria-hidden="true"><circle cx="6" cy="6" r="5.3" fill="none" stroke="#fff"/><ellipse cx="6" cy="6" rx="2.3" ry="5.3" fill="none" stroke="#fff"/><path d="M0.7 6 H11.3" stroke="#fff"/></svg>
        www.gravelmothco.ca
      </li>
    </ul>
  </section>

  <section class="card card--brand">
    <div class="rock-texture" role="img" aria-label="Grey and olive rock surface texture with dust specks"></div>
    <span class="brand-emblem" aria-hidden="true"></span>
    <div class="brand-lockup">
      <div class="wordmark">Gravelmoth Co.</div>
      <p class="tagline">clothing</p>
    </div>
  </section>
</body>
</html>
```